依頼詳細
デザインテイストのイメージは以下の通りです
・洗練された
・安心感のある
・落ち着いた
・信頼できる

「写真素材について」
事業所画像など一部提供可能ですが、基本的にはミルテフォトなどの素材もしくはイラストとの組み合わせでお願いいたします

「WFと原稿について」
レイアウトについてはある程度自由に変更していただいても結構です

「納品形態について」
psd xd aiなど劣化のないものであればなんでも大丈夫です

「選考のポイント」
デザイン性のみ
SEOやマーケティング的な提案は求めていません
元サイトURL一応載せておきますが形式的に作成したものですので
こちらと比較してのアドバイスなども求めていません
あくまでデザインで決めます

サイトURL
http://kurete-kaigo.net/
ページ数
5ページ
希望イメージ
シンプル 複雑
単色 カラフル
暗い 明るい
日常 高級
遊び心 厳粛
未来的 伝統的
女性的 男性的
希望する色
青系、水色系
納品ファイル
• 高解像度JPG (.jpg)
• イラストレーター形式 (.ai)
• フォトショップ形式 (.psd)
• PNG形式 (.png)
補足説明
提案の数が少ないので期限を延長いたします
■ 選んだ理由

限定された条件のなかで素晴らしいデザインをご提案いただきありがとうございました

■ 提案者全員のお礼・コメント

素材画像がない状態でのデザイン制作は難しかったと思います
その中で素晴らしい提案をいただきまして本当にありがとうございました

```html
<!DOCTYPE html>
<html lang="ja">
<head>
<meta charset="utf-8">
<title>訪問介護そよかぜ</title>
<link href="https://fonts.googleapis.com/css2?family=Noto+Sans+JP:wght@400;500;700&family=Noto+Serif+JP:wght@500;700&display=swap" rel="stylesheet">
<style>
:root{
  --blue:#23a0e0;
  --blue-dark:#1a86c4;
  --blue-deep:#0f6fa8;
  --blue-pale:#e6f4fc;
  --beige:#f5efe3;
  --ink:#3f4a52;
  --muted:#7b8790;
  --white:#ffffff;
  --photo-a:#cfe6f3;
  --photo-b:#efe3d0;
}
*{box-sizing:border-box;margin:0;padding:0}
html,body{width:1200px;height:3744px;overflow:hidden}
body{position:relative;font-family:"Noto Sans JP",sans-serif;color:var(--ink);background:var(--white);font-size:14px;line-height:1.8}
.abs{position:absolute}
.ph{position:absolute;background:linear-gradient(135deg,var(--photo-a),var(--photo-b))}
.illus{position:absolute;background:linear-gradient(160deg,#d8ecf8,#f3e6d6);border-radius:40px}
.btn{display:inline-block;background:var(--blue);color:var(--white);font-size:13px;padding:8px 34px;border-radius:30px;font-weight:500}
.btn-center{position:absolute;left:50%;transform:translateX(-50%)}

/* hero */
.hero{left:0;top:0;width:1200px;height:470px;background:linear-gradient(120deg,#9fcbe6 0%,#c9b79c 45%,#b7a88f 55%,#8fc2e2 100%)}
.hero-shade{left:0;top:40px;width:1200px;height:130px;background:linear-gradient(90deg,rgba(15,111,168,0) 0%,rgba(15,111,168,.35) 25%,rgba(15,111,168,.35) 75%,rgba(15,111,168,0) 100%)}
.hero-copy{left:0;top:48px;width:1200px;text-align:center;color:var(--white);text-shadow:0 0 8px var(--blue-deep),0 0 3px var(--blue-deep),0 2px 4px rgba(0,0,0,.35)}
.hero-copy .lead{font-size:44px;font-weight:700;letter-spacing:.04em;line-height:1.3}
.hero-copy .sub{font-size:34px;font-weight:700;line-height:1.4}
.hero-cta{left:0;top:180px;width:1200px;display:flex;justify-content:center;gap:18px}
.cta-tel{background:var(--blue);color:var(--white);width:220px;height:60px;border-radius:6px;text-align:center;padding-top:6px}
.cta-tel b{display:block;font-size:22px;line-height:1.2;letter-spacing:.03em}
.cta-tel small{font-size:10px}
.cta-mail{background:var(--white);color:var(--blue);border:2px solid var(--blue);width:220px;height:60px;border-radius:6px;display:flex;align-items:center;justify-content:center;font-weight:700;font-size:15px;gap:8px}
.logo{left:540px;top:360px;width:120px;height:120px;background:var(--blue);border-radius:10px;display:flex;flex-direction:column;align-items:center;justify-content:center;gap:8px;color:var(--white);font-weight:700;font-size:20px}
.logo i{width:34px;height:34px;border-radius:50%;background:var(--white)}

.gnav{left:180px;top:500px;width:840px;display:flex;justify-content:space-between}
.gnav a{width:96px;text-align:center;color:var(--ink);font-size:12px;text-decoration:none}
.gnav svg{display:block;margin:0 auto 6px;width:44px;height:44px}

/* features */
.features{left:0;top:600px;width:1200px;height:700px;background:var(--beige)}
.hand-l{left:200px;top:620px;width:140px;height:640px;border-radius:0 0 70px 70px;opacity:.55}
.hand-r{left:860px;top:620px;width:140px;height:640px;border-radius:0 0 70px 70px;opacity:.55}
.paper{left:280px;top:650px;width:640px;height:560px;background:var(--white);border:2px solid #cfe3ef;border-radius:4px}
.sec-title-serif{font-family:"Noto Serif JP",serif;color:var(--blue);font-size:26px;text-align:center;font-weight:700;letter-spacing:.06em}
.feat{width:260px}
.feat h3{font-family:"Noto Serif JP",serif;color:var(--blue);font-size:15px;text-align:center;margin-bottom:10px;font-weight:700}
.feat p{font-size:12px;line-height:1.9;color:var(--ink)}

/* services */
.services{left:0;top:1320px;width:1200px;height:880px;background:var(--blue)}
.sec-title-white{color:var(--white);font-size:26px;font-weight:700;letter-spacing:.1em}
.card{position:absolute;background:var(--white);border-radius:8px;padding:28px 34px}
.card h3{color:var(--blue);font-size:18px;text-align:center;margin-bottom:12px}
.card p{font-size:12px;line-height:1.9;margin-bottom:18px}

/* usage */
.usage{left:0;top:2200px;width:1200px;height:470px;background:linear-gradient(180deg,#fff,var(--blue-pale))}
.usage-title{left:500px;top:2240px;width:200px;height:44px;border:2px solid var(--blue);color:var(--blue);font-size:22px;font-weight:700;text-align:center;line-height:40px;background:var(--white)}
.usage-card{left:300px;top:2310px;width:500px;height:250px;background:var(--white);border:1px solid #cfe3ef;border-radius:8px;padding:30px 40px;text-align:center}
.usage-card h3{color:var(--blue);font-size:17px;margin-bottom:10px}
.usage-card p{font-size:12px;text-align:left;margin-bottom:20px}

/* contact band */
.contact{left:0;top:2680px;width:1200px;height:190px;background:var(--blue)}
.contact-box{left:260px;top:2705px;width:680px;height:140px;background:var(--white);border-radius:6px;text-align:center;padding-top:18px}
.contact-box h2{color:var(--blue);font-size:20px;font-weight:700;margin-bottom:12px}
.contact-row{display:flex;justify-content:center;gap:18px}

/* news */
.news-title{left:0;top:2920px;width:1200px;text-align:center;color:var(--blue);font-size:26px;font-weight:700}
.news-card{position:absolute;top:2990px;width:220px;height:170px;background:var(--white);border:1px solid #d9e6ee;border-radius:6px;overflow:hidden}
.news-card .ph{position:relative;height:96px}
.news-card .meta{font-size:10px;color:var(--muted);padding:8px 12px 0}
.news-card .meta span{background:var(--blue);color:var(--white);padding:1px 6px;border-radius:2px;margin-right:6px}
.news-card p{font-size:12px;padding:2px 12px}
.arrow{position:absolute;top:3060px;width:24px;height:24px}

/* recruit */
.recruit{left:0;top:3260px;width:1200px;height:420px;background:var(--blue)}
.recruit-title{left:0;top:3290px;width:1200px;text-align:center;color:var(--white);font-size:34px;font-weight:700;letter-spacing:.06em}
.recruit-sub{left:0;top:3346px;width:1200px;text-align:center;color:var(--white);font-size:15px}
.point{position:absolute;top:3392px;width:190px;height:190px;border-radius:50%;background:var(--white);display:flex;flex-direction:column;align-items:center;justify-content:center;text-align:center;padding:18px;font-size:11px;color:var(--ink);line-height:1.7}
.point b{color:var(--blue);font-size:13px;margin-bottom:6px;line-height:1.5;white-space:nowrap}
.btn-white{background:var(--white);color:var(--blue)}

/* footer */
.footer-nav{left:0;top:3690px;width:1200px;display:flex;justify-content:center;gap:40px;font-size:12px}
.copyright{left:0;top:3722px;width:1200px;height:22px;background:var(--blue);color:var(--white);font-size:10px;text-align:center;line-height:22px}
</style>
</head>
<body>

<!-- hero -->
<div class="abs hero" role="img" aria-label="写真：介護スタッフが自宅で高齢の女性と笑顔で話している様子"></div>
<div class="abs hero-shade"></div>
<div class="abs hero-copy">
  <div class="lead">24時間365日</div>
  <div class="sub">住み慣れたご自宅で"自分らしい"介護サービスを</div>
</div>
<div class="abs hero-cta">
  <div class="cta-tel"><b>098-555-0142</b><small>受付 9:00〜18:00</small></div>
  <div class="cta-mail">
    <svg width="20" height="16" viewBox="0 0 20 16"><rect x="1" y="1" width="18" height="14" rx="2" fill="none" stroke="currentColor" stroke-width="2"/><path d="M1 2l9 7 9-7" fill="none" stroke="currentColor" stroke-width="2"/></svg>
    メールでお問い合わせ
  </div>
</div>
<div class="abs logo"><i></i>そよかぜ</div>

<nav class="abs gnav">
  <a><svg viewBox="0 0 44 44"><circle cx="22" cy="22" r="20" fill="var(--blue-pale)"/><path d="M22 31s-9-5.5-9-11a5 5 0 0 1 9-3 5 5 0 0 1 9 3c0 5.5-9 11-9 11z" fill="var(--blue)"/></svg>理念</a>
  <a><svg viewBox="0 0 44 44"><circle cx="22" cy="22" r="20" fill="var(--blue-pale)"/><rect x="14" y="12" width="16" height="20" rx="2" fill="none" stroke="var(--blue)" stroke-width="2"/><path d="M17 18h10M17 23h10M17 28h6" stroke="var(--blue)" stroke-width="2"/></svg>ご利用について</a>
  <a><svg viewBox="0 0 44 44"><circle cx="22" cy="22" r="20" fill="var(--blue-pale)"/><path d="M12 30h20v-8l-10-8-10 8z" fill="none" stroke="var(--blue)" stroke-width="2"/></svg>提供サービス</a>
  <a><svg viewBox="0 0 44 44"><circle cx="22" cy="22" r="20" fill="var(--blue-pale)"/><circle cx="22" cy="22" r="9" fill="none" stroke="var(--blue)" stroke-width="2"/><path d="M22 17v5l3 3" stroke="var(--blue)" stroke-width="2" fill="none"/></svg>よくある質問</a>
  <a><svg viewBox="0 0 44 44"><circle cx="22" cy="22" r="20" fill="var(--blue-pale)"/><path d="M22 12a7 7 0 0 1 7 7c0 5-7 13-7 13s-7-8-7-13a7 7 0 0 1 7-7z" fill="var(--blue)"/><circle cx="22" cy="19" r="2.5" fill="#fff"/></svg>事業所一覧</a>
  <a><svg viewBox="0 0 44 44"><circle cx="22" cy="22" r="20" fill="var(--blue-pale)"/><circle cx="22" cy="17" r="5" fill="var(--blue)"/><path d="M13 32a9 9 0 0 1 18 0z" fill="var(--blue)"/></svg>採用情報</a>
  <a><svg viewBox="0 0 44 44"><circle cx="22" cy="22" r="20" fill="var(--blue-pale)"/><rect x="14" y="14" width="16" height="18" fill="none" stroke="var(--blue)" stroke-width="2"/><path d="M18 19h2M24 19h2M18 24h2M24 24h2" stroke="var(--blue)" stroke-width="2"/></svg>運営会社</a>
</nav>

<!-- features -->
<div class="abs features"></div>
<div class="illus hand-l" role="img" aria-label="イラスト：紙を支える左手の線画"></div>
<div class="illus hand-r" role="img" aria-label="イラスト：紙を支える右手の線画"></div>
<div class="abs paper"></div>
<h2 class="abs sec-title-serif" style="left:280px;top:690px;width:640px">訪問介護そよかぜの特徴</h2>
<div class="abs feat" style="left:330px;top:770px">
  <h3>24時間365日対応</h3>
  <p>早朝や深夜、休日でも必要な時にいつでも訪問いたします。急な体調の変化にも担当スタッフが落ち着いて対応し、ご家族の負担を減らします。夜間の見守りや定期的な巡回にも対応しており、ひとり暮らしの方も安心してお過ごしいただけます。</p>
</div>
<div class="abs feat" style="left:610px;top:770px">
  <h3>ひとりひとりに最適な介護を提供</h3>
  <p>ご本人の生活リズムやご希望を丁寧にうかがい、無理のないケアプランを作成します。状況に合わせて内容を見直し、安心を支えます。ご家族との情報共有も欠かさず、チーム全体で日々の暮らしを見守ります。</p>
</div>
<div class="abs feat" style="left:330px;top:985px;width:540px">
  <h3>お客様だけに寄り添う介護を</h3>
  <p>経験豊富なスタッフが同じ目線でお話をうかがい、住み慣れたご自宅での暮らしを大切にします。できることはご自身で続けられるよう、さりげなく寄り添いながらお手伝いいたします。小さな不安もお気軽にご相談ください。</p>
</div>
<span class="btn btn-center" style="top:1140px">特徴を見る</span>

<!-- services -->
<div class="abs services"></div>
<h2 class="abs sec-title-white" style="left:0;top:1350px;width:1200px;text-align:center">提供サービス</h2>
<div class="ph" style="left:140px;top:1420px;width:420px;height:280px;border-radius:8px" role="img" aria-label="写真：スタッフが高齢男性の歩行を支えている様子"></div>
<div class="illus" style="left:40px;top:1560px;width:130px;height:180px" role="img" aria-label="イラスト：歩行を支え合う高齢夫婦"></div>
<div class="card" style="left:600px;top:1450px;width:480px;height:220px">
  <h3>訪問介護</h3>
  <p>ホームヘルパーがご自宅を訪問し、食事や入浴、排せつの介助から掃除や買い物などの生活援助まで幅広くお手伝いします。</p>
  <div style="text-align:center"><span class="btn">詳しく見る</span></div>
</div>
<div class="card" style="left:140px;top:1800px;width:480px;height:220px">
  <h3>居宅介護支援</h3>
  <p>ケアマネジャーがご本人とご家族のお話をうかがい、最適なケアプランを作成。各サービス事業者との連絡や調整も行います。</p>
  <div style="text-align:center"><span class="btn">詳しく見る</span></div>
</div>
<div class="ph" style="left:680px;top:1760px;width:300px;height:300px;border-radius:50%" role="img" aria-label="写真：車いすの利用者とスタッフが会話している様子"></div>
<div class="illus" style="left:1000px;top:1860px;width:130px;height:200px" role="img" aria-label="イラスト：車いすを押す介護スタッフ"></div>

<!-- usage -->
<div class="abs usage"></div>
<div class="abs usage-title">ご利用について</div>
<div class="abs usage-card">
  <h3>訪問介護のご利用には要介護認定が必要です</h3>
  <p>まずはお住まいの地域の窓口で申請を行い、認定を受けた後にケアプランを作成します。手続きがわからない場合もお気軽にご相談ください。</p>
  <span class="btn">ご利用の流れを見る</span>
</div>
<div class="illus" style="left:840px;top:2330px;width:130px;height:310px" role="img" aria-label="イラスト：白衣の看護スタッフ"></div>

<!-- contact -->
<div class="abs contact"></div>
<div class="illus" style="left:50px;top:2690px;width:150px;height:180px" role="img" aria-label="イラスト：手を挙げる男性スタッフ"></div>
<div class="illus" style="left:1000px;top:2690px;width:150px;height:180px" role="img" aria-label="イラスト：案内する女性スタッフ"></div>
<div class="abs contact-box">
  <h2>無料相談受付中！お気軽にお問い合わせください</h2>
  <div class="contact-row">
    <div class="cta-tel"><b>098-555-0142</b><small>受付 9:00〜18:00</small></div>
    <div class="cta-mail" style="background:var(--blue);color:var(--white)">
      <svg width="20" height="16" viewBox="0 0 20 16"><rect x="1" y="1" width="18" height="14" rx="2" fill="none" stroke="currentColor" stroke-width="2"/><path d="M1 2l9 7 9-7" fill="none" stroke="currentColor" stroke-width="2"/></svg>
      メールでお問い合わせ
    </div>
  </div>
</div>

<!-- news -->
<h2 class="abs news-title">お知らせ</h2>
<svg class="arrow" style="left:185px" viewBox="0 0 24 24"><path d="M16 3L7 12l9 9" fill="none" stroke="var(--blue)" stroke-width="3"/></svg>
<div class="news-card" style="left:240px"><div class="ph" role="img" aria-label="写真：明るい施設の食堂"></div><div class="meta"><span>お知らせ</span>2024.04.01</div><p>新事業所開設のお知らせ</p></div>
<div class="news-card" style="left:490px"><div class="ph" role="img" aria-label="写真：笑顔で働くスタッフ"></div><div class="meta"><span>お知らせ</span>2024.03.15</div><p>スタッフ研修を実施しました</p></div>
<div class="news-card" style="left:740px"><div class="ph" role="img" aria-label="写真：看護スタッフ"></div><div class="meta"><span>お知らせ</span>2024.03.01</div><p>営業時間変更のご案内</p></div>
<svg class="arrow" style="left:991px" viewBox="0 0 24 24"><path d="M8 3l9 9-9 9" fill="none" stroke="var(--blue)" stroke-width="3"/></svg>
<span class="btn btn-center" style="top:3185px">一覧を見る</span>

<!-- recruit -->
<div class="abs recruit"></div>
<h2 class="abs recruit-title">スタッフ積極採用中！</h2>
<p class="abs recruit-sub">「介護はそよかぜにお願いしたい」地域の皆様の声にお応えするために！</p>
<div class="illus" style="left:40px;top:3380px;width:220px;height:280px" role="img" aria-label="イラスト：スタッフと車いすの利用者"></div>
<div class="point" style="left:300px"><b>未経験・ブランクも歓迎</b>研修制度で基礎から<br>しっかり学べます</div>
<div class="point" style="left:505px"><b>働き方を選べる勤務体系</b>日勤のみや短時間の<br>勤務もご相談ください</div>
<div class="point" style="left:710px"><b>資格取得支援制度あり</b>費用補助でスタッフの<br>成長を応援します</div>
<div class="illus" style="left:940px;top:3380px;width:220px;height:280px" role="img" aria-label="イラスト：笑顔の介護スタッフたち"></div>
<span class="btn btn-white btn-center" style="top:3610px">採用情報</span>

<!-- footer -->
<nav class="abs footer-nav">
  <span>理念</span><span>ご利用について</span><span>提供サービス</span><span>よくある質問</span><span>事業所一覧</span><span>採用情報</span><span>運営会社</span>
</nav>
<div class="abs copyright">Copyright © 訪問介護そよかぜ All Rights Reserved.</div>

</body>
</html>
```